CareJure Chambers Mailer for Small Medical Offices and Solo Physician Practices

CareJure Chambers -- We are a local health law firm looking to provide advice to medical practices on the legal issues they face. We strive to function as a general counsel for medical practices and provide tailored solutions to meet the needs of our clients. Please see postcard content ideas in document attached. Our firm colors are royal blue, gray and white and black.

Target Market(s)

Small medical offices, solo physician practices in the Southeast Michigan (Detroit Metro area)

Industry/Entity Type

Law Firm

Font styles to use
Sans Serif

Colors
0991cd
3176b5
ffffff
7f7f7f
1b1b1b

Requirements
Must have
• Brief summary of legal services offered, bullet pointed list of practice areas/issues
• Contact information, website, address
• Pictures of attorneys
• Prefer the use of our firm's colors (royal blue, gray, white, black)
Nice to have
• Included some purchased stock images that could also be incorporated

```html
<!DOCTYPE html>
<html lang="en">
<head>
<meta charset="utf-8">
<title>CareJure Chambers – Health Law Mailer</title>
<link href="https://fonts.googleapis.com/css2?family=Jost:wght@700&family=Nunito+Sans:wght@300;400;700;800&family=Oswald:wght@500;600&display=swap" rel="stylesheet">
<style>
  :root {
    --mat: #1b1b1b;
    --paper: #ffffff;
    --royal: #0b66b2;
    --sky: #1fa7e6;
    --tick: #3fb6ee;
    --deep-link: #1565b0;
    --gray: #7f7f7f;
    --ink: #ffffff;
  }
  * { box-sizing: border-box; margin: 0; padding: 0; }
  html, body { width: 1200px; height: 727px; overflow: hidden; background: var(--mat); }
  body { font-family: "Nunito Sans", Arial, sans-serif; position: relative; }

  .mailer {
    position: absolute; left: 92px; top: 86px;
    width: 1016px; height: 554px;
    background: var(--paper); overflow: hidden;
  }
  .mailer > * { position: absolute; }

  .blue-field { left: 0; top: 0; width: 1016px; height: 554px; }

  .stock-photo {
    left: 590px; top: 100px; width: 426px; height: 454px;
    background: radial-gradient(ellipse at 45% 55%, #6b4a34 0%, #8a6a50 18%, #cfc6bf 45%, #f4f4f4 70%, #ffffff 100%);
  }

  .headline {
    left: 48px; top: 26px;
    font-family: "Jost", "Futura", sans-serif; font-weight: 700;
    font-size: 61px; line-height: 62px; letter-spacing: 1px;
    color: var(--ink);
  }

  .intro {
    left: 46px; top: 160px; width: 580px;
    font-weight: 300; font-size: 15.5px; line-height: 19px; color: var(--ink);
  }

  .services {
    left: 46px; top: 207px; list-style: none;
    font-weight: 800; font-size: 15px; line-height: 20.6px; color: var(--ink);
  }
  .services li { display: flex; align-items: center; gap: 5px; }
  .services svg { width: 12px; height: 12px; flex: none; }

  .closing {
    left: 41px; top: 424px; width: 470px;
    font-weight: 300; font-size: 15.5px; line-height: 19px; color: var(--ink);
  }

  .call-pill {
    left: 61px; top: 497px; width: 272px; height: 27px;
    border: 1.5px solid var(--sky); border-radius: 14px;
    font-weight: 300; font-size: 16px; line-height: 24px;
    color: var(--ink); text-align: center;
  }

  .free-badge {
    left: 401px; top: 234px; width: 160px; height: 160px;
    border-radius: 50%; background: var(--sky);
    font-family: "Oswald", sans-serif; color: var(--ink);
    text-align: center; text-transform: uppercase;
    display: flex; flex-direction: column; justify-content: center;
  }
  .free-badge .big { font-size: 50px; line-height: 50px; font-weight: 600; }
  .free-badge .small { font-size: 21px; line-height: 24px; font-weight: 500; }

  .phone {
    left: 420px; top: 490px; width: 310px; text-align: center;
    font-weight: 800; font-size: 25px; letter-spacing: 0.5px; color: var(--sky);
  }
  .website {
    left: 420px; top: 521px; width: 310px; text-align: center;
    font-weight: 800; font-size: 15.5px; color: var(--deep-link);
  }

  .brand {
    right: 42px; top: 36px;
    display: flex; align-items: center; gap: 14px;
  }
  .brand-name {
    font-family: "Nunito Sans", Arial, sans-serif; font-weight: 400;
    font-size: 32px; color: var(--gray);
  }
  .brand-mark { width: 38px; height: 38px; background: var(--gray); }
</style>
</head>
<body>
  <main class="mailer">
    <div class="stock-photo" role="img" aria-label="Stock photo of a wooden judge's gavel with a brass band lying on a black stethoscope"></div>

    <svg class="blue-field" viewBox="0 0 1016 554" aria-hidden="true">
      <path d="M0 0 H563 C640 110 640 360 428 554 H0 Z" fill="var(--royal)"/>
    </svg>

    <div class="brand">
      <span class="brand-name">CareJure Chambers</span>
      <span class="brand-mark"></span>
    </div>

    <h1 class="headline">HEALTH LAW<br>QUESTIONS?</h1>

    <p class="intro">We are local, experienced health lawyers available to provide efficient, effective advice on the issues impacting your healthcare business every day, including:</p>

    <ul class="services">
      <li><svg viewBox="0 0 12 12"><path d="M1.5 6.5 L4.5 9.5 L10.5 2.5" fill="none" stroke="var(--tick)" stroke-width="2"/></svg>Contract review and negotiation</li>
      <li><svg viewBox="0 0 12 12"><path d="M1.5 6.5 L4.5 9.5 L10.5 2.5" fill="none" stroke="var(--tick)" stroke-width="2"/></svg>Stark and Anti-kickback matters</li>
      <li><svg viewBox="0 0 12 12"><path d="M1.5 6.5 L4.5 9.5 L10.5 2.5" fill="none" stroke="var(--tick)" stroke-width="2"/></svg>Reimbursement and payer issues</li>
      <li><svg viewBox="0 0 12 12"><path d="M1.5 6.5 L4.5 9.5 L10.5 2.5" fill="none" stroke="var(--tick)" stroke-width="2"/></svg>HIPAA</li>
      <li><svg viewBox="0 0 12 12"><path d="M1.5 6.5 L4.5 9.5 L10.5 2.5" fill="none" stroke="var(--tick)" stroke-width="2"/></svg>Vendor issues</li>
      <li><svg viewBox="0 0 12 12"><path d="M1.5 6.5 L4.5 9.5 L10.5 2.5" fill="none" stroke="var(--tick)" stroke-width="2"/></svg>Licensing matters</li>
      <li><svg viewBox="0 0 12 12"><path d="M1.5 6.5 L4.5 9.5 L10.5 2.5" fill="none" stroke="var(--tick)" stroke-width="2"/></svg>Employee issues</li>
      <li><svg viewBox="0 0 12 12"><path d="M1.5 6.5 L4.5 9.5 L10.5 2.5" fill="none" stroke="var(--tick)" stroke-width="2"/></svg>Difficult patient matters</li>
      <li><svg viewBox="0 0 12 12"><path d="M1.5 6.5 L4.5 9.5 L10.5 2.5" fill="none" stroke="var(--tick)" stroke-width="2"/></svg>Subpoenas and medical record requests</li>
      <li><svg viewBox="0 0 12 12"><path d="M1.5 6.5 L4.5 9.5 L10.5 2.5" fill="none" stroke="var(--tick)" stroke-width="2"/></svg>Leases and landlord-tenant issues</li>
    </ul>

    <p class="closing">We provide personalized service to our clients so you have trusted counsel available when you need it.&nbsp; We offer competitive hourly rates as well as flat fee arrangements when possible.</p>

    <div class="call-pill">For More information Call Today</div>

    <div class="free-badge">
      <span class="big">Free</span>
      <span class="small">Consultations<br>Available</span>
    </div>

    <div class="phone">248.555.0174</div>
    <div class="website">www.carejurechambers.com</div>
  </main>
</body>
</html>
```